Harbor Advance, Inc.

We need a website design for a new company based in Orange County, CA but will be serving client's throughout all of California. We provide non-recourse loans/ pre-litigation funding for client's in personal injury and employment cases. Generally, if a client has an active case and they need money for cost of living, the client will contact a company like ours to provide a loan. We would like to see designs that are sleek, simple and easy to use. The final design should communicate trustworthiness, financial safety and promptness.

Hi, I like KW's designs. I am having him work on a hybrid of two of his designs. We had a little miscommunication, but we are almost there. Best, Ned

```html
<!DOCTYPE html>
<html lang="en">
<head>
<meta charset="utf-8">
<title>Harbor Advance, Inc.</title>
<link href="https://fonts.googleapis.com/css2?family=Jost:wght@300;400;500&display=swap" rel="stylesheet">
<style>
:root{
  --red:#d42027;
  --red-band:#dc3a40;
  --ink:#333333;
  --muted:#555555;
  --white:#ffffff;
  --card:#ececec;
  --stage:#efefef;
  --hero-dark:#3d2e28;
  --hero-mid:#6b5a50;
}
*{box-sizing:border-box;margin:0;padding:0}
html,body{width:1200px;height:960px;overflow:hidden}
body{background:var(--stage);font-family:"Jost",sans-serif;color:var(--ink);position:relative}
.page{position:absolute;left:279px;top:54px;width:642px;height:906px;background:var(--white);overflow:hidden}
.nav{position:absolute;left:0;top:0;width:642px;height:31px;background:var(--white);z-index:3}
.brand{position:absolute;left:20px;top:4px;font-size:19px;font-weight:400;color:var(--red);letter-spacing:-.3px}
.brand small{font-size:10px}
.nav-link{position:absolute;top:11px;font-size:7.5px;color:var(--ink);text-transform:uppercase}
.nav-cta{position:absolute;left:548px;top:8px;width:73px;height:18px;background:var(--red);color:var(--white);font-size:7.5px;display:flex;align-items:center;justify-content:center}
.hero-photo{position:absolute;left:0;top:31px;width:642px;height:875px;background:linear-gradient(180deg,#7d6658 0%,#5a463c 30%,var(--hero-dark) 55%,#2e2420 100%)}
.hero-photo.side{background:linear-gradient(90deg,#3a2d27 0%,#5a4a42 50%,#3a2d27 100%)}
.hero-text{position:absolute;left:20px;top:148px;width:402px;text-align:center;color:var(--white);font-size:19px;line-height:24px;font-weight:400;z-index:2}
.hero-btn{position:absolute;left:162px;top:253px;width:120px;height:24px;border:1px solid var(--white);border-radius:2px;color:var(--white);font-size:11.5px;display:flex;align-items:center;justify-content:center;z-index:2}
.consult{position:absolute;left:441px;top:31px;width:201px;height:336px;background:rgba(120,110,105,.55);z-index:2}
.consult h2{position:absolute;left:0;top:25px;width:201px;text-align:center;color:var(--white);font-weight:400;font-size:16px;line-height:19px}
.field{position:absolute;left:19px;width:162px;height:22px;background:var(--white);border-radius:2px;font-size:8px;font-style:italic;color:#9a9a9a;padding:6px 9px}
.field.details{height:69px}
.consult-btn{position:absolute;left:18px;top:280px;width:163px;height:24px;background:var(--red);color:var(--white);font-size:11.5px;display:flex;align-items:center;justify-content:center}
.content{position:absolute;left:43px;top:367px;width:555px;height:560px;background:var(--white);border-radius:13px 13px 0 0;z-index:2}
.section-title{position:absolute;left:0;width:555px;text-align:center;font-size:24px;font-weight:400;color:var(--ink);letter-spacing:-.3px}
.rule{position:absolute;left:268px;width:18px;height:1.5px;background:var(--red)}
.steps{position:absolute;left:0;top:457px;z-index:3}
.step-num{position:absolute;font-size:11px;color:var(--ink);z-index:4}
.step-title{position:absolute;font-size:11.5px;color:var(--ink);z-index:4}
.step-desc{position:absolute;font-size:6.5px;line-height:9.6px;color:var(--muted);width:115px;z-index:4}
.card{position:absolute;top:309px;width:155px;height:200px;background:var(--card)}
.card h3{position:absolute;left:0;top:22px;width:155px;text-align:center;font-weight:400;font-size:16px;line-height:19px;color:var(--ink)}
.card .rule{left:69px;top:69px}
.card p{position:absolute;left:13px;top:90px;width:129px;font-size:6.8px;line-height:9.6px;color:var(--muted);text-align:justify}
.card-btn{position:absolute;left:18px;top:162px;width:118px;height:24px;background:var(--red);color:var(--white);font-size:11.5px;display:flex;align-items:center;justify-content:center}
</style>
</head>
<body>
<div class="page">
  <header class="nav">
    <div class="brand">harbor advance <small>inc</small></div>
    <span class="nav-link" style="left:263px">Home</span>
    <span class="nav-link" style="left:323px">About</span>
    <span class="nav-link" style="left:383px">Customer Reviews</span>
    <span class="nav-link" style="left:491px">Contact</span>
    <span class="nav-cta">APPLY NOW</span>
  </header>

  <div class="hero-photo" role="img" aria-label="Photo of a smiling advisor in a suit presenting to clients around a meeting table in an office"></div>

  <p class="hero-text">We provide non-recourse loans/ pre-litigation funding for your in personal injury and employment cases.</p>
  <div class="hero-btn">Find out more...</div>

  <form class="consult">
    <h2>Apply Now for your free legal funding consultation</h2>
    <div class="field" style="top:80px">name</div>
    <div class="field" style="top:110px">phone</div>
    <div class="field" style="top:139px">email</div>
    <div class="field" style="top:169px">-Select funding type-</div>
    <div class="field details" style="top:198px">Details</div>
    <div class="consult-btn">Apply Now!</div>
  </form>

  <section class="content">
    <h2 class="section-title" style="top:28px">HOW HARBOR ADVANCE</h2>
    <div class="rule" style="top:67px"></div>

    <h2 class="section-title" style="top:236px">APPLY NOW</h2>
    <div class="rule" style="top:271px"></div>

    <article class="card" style="left:27px">
      <h3>Attorney Fee<br>Acceleration</h3>
      <div class="rule"></div>
      <p>Our proprietary program that converts settled cases into immediate cash. No more waiting for slow-paying defendants, administrative delays, or court approvals.</p>
      <div class="card-btn">Apply Now!</div>
    </article>
    <article class="card" style="left:207px">
      <h3>Attorney's Line<br>of Credit</h3>
      <div class="rule"></div>
      <p>At Harbor Advance Inc, there's no credit crisis! We are ready and able to deliver the affordable line of credit you need. Lines up to $10 million or more.</p>
      <div class="card-btn">Apply Now!</div>
    </article>
    <article class="card" style="left:388px">
      <h3>Plaintiff Settlement<br>Funding</h3>
      <div class="rule"></div>
      <p>Are you a plaintiff with a settled case, but tired of waiting to get paid? Harbor Advance Inc now offers non-recourse post-settlement funding to plaintiffs.</p>
      <div class="card-btn">Apply Now!</div>
    </article>
  </section>

  <svg class="steps" width="642" height="110" viewBox="0 457 642 110" aria-hidden="true">
    <rect x="0" y="477" width="642" height="67" fill="var(--red-band)"/>
    <polygon points="31,457 177,457 226,510 177,564 31,564" fill="#fff" stroke="var(--red)" stroke-width="1.3"/>
    <polygon points="177,457 373,457 422,510 373,564 177,564 226,510" fill="#fff" stroke="var(--red)" stroke-width="1.3"/>
    <polygon points="373,457 570,457 620,510 570,564 373,564 422,510" fill="#fff" stroke="var(--red)" stroke-width="1.3"/>
  </svg>
  <span class="step-num" style="left:35px;top:473px">01</span>
  <span class="step-title" style="left:57px;top:490px">Apply Online</span>
  <span class="step-desc" style="left:57px;top:512px">Fill out our free consultation application.</span>
  <span class="step-num" style="left:234px;top:473px">02</span>
  <span class="step-title" style="left:255px;top:490px">Consult with Us</span>
  <span class="step-desc" style="left:255px;top:512px">Consult with our legal funding officers.</span>
  <span class="step-num" style="left:430px;top:473px">03</span>
  <span class="step-title" style="left:453px;top:485px">Get Funded</span>
  <span class="step-desc" style="left:453px;top:508px">If your application is approved, we'll deposit your money as early as the next business day.</span>
</div>
</body>
</html>
```